Investment Group needs a web page design

We need a web page design for a San Francisco-based investment group called 'Talvirow LLC'. The final design should be stylish and attractive to the idea while retaining a sense of stability and professionalism. A great example is http://brambleharborgroup.com/.

I am attaching the group's logo which should be the base for the webpage design.
Updates

Please note that I am interested in a single webpage that presents basic information. See the following example: http://brambleharborgroup.com/

Target Market(s)

persons doing initial due diligence and trying to assess what kind of group we are.

Industry/Entity Type

Investment

Font styles to use
Serif

Colors
86acd3
3176b5
0355a3

Requirements
Nice to have
• Would love the design to incorporate the concept - 'Talvirow: a block and counter attack while the opponent is attacking.'
Should not have
• Do not include trite illustrations related to finance, money or investing.

```html
<!DOCTYPE html>
<html lang="en">
<head>
<meta charset="utf-8">
<title>Talvirow LLC – Investment Group</title>
<link rel="stylesheet" href="https://fonts.googleapis.com/css2?family=Open+Sans:ital,wght@0,300;0,400;0,600;0,700;1,400&family=PT+Serif:wght@400;700&display=swap">
<style>
:root{
  --blue:#3b7cc4;
  --blue-deep:#2f6fb3;
  --blue-dark:#0355a3;
  --blue-soft:#86acd3;
  --ink:#222;
  --text:#444;
  --muted:#777;
  --band:#ececec;
  --panel:#f4f4f4;
  --charcoal:#3a3a3a;
  --button-dark:#333;
  --teal:#1f7c99;
  --accent:#e8c21b;
  --white:#fff;
}
*{margin:0;padding:0;box-sizing:border-box}
html,body{width:1200px;height:2712px;overflow:hidden}
body{font-family:"Open Sans",sans-serif;color:var(--text);background:var(--white);position:relative}
section,header,footer{position:absolute;left:0;width:1200px}
.abs{position:absolute}

/* header */
.site-header{top:0;height:163px;background:var(--blue)}
.brand{left:102px;top:66px;display:flex;align-items:center;gap:14px}
.brand-mark{width:42px;height:42px;background:#111;border-radius:4px}
.brand-name{font-size:44px;font-weight:400;color:#111;letter-spacing:1px;line-height:1}
.social-top{right:103px;top:11px;display:flex;gap:6px}
.social-top span{width:28px;height:28px;border-radius:50%;background:var(--white)}
.main-nav{left:675px;top:100px;display:flex;gap:40px;font-size:15px;color:var(--white)}
.main-nav .current{color:#e9e36a}

/* hero */
.hero{top:163px;height:470px;background:linear-gradient(100deg,#5a6c80 0%,#b8c4d0 35%,#d7dde4 60%,#9fa9b3 100%);overflow:hidden}
.hero-photo{inset:0}
.hero-caption{left:100px;top:273px;width:560px;height:150px;background:rgba(40,40,40,.55);color:var(--white);padding:10px 14px;font-size:40px;line-height:1.1;font-weight:300;white-space:nowrap}
.hero-caption .l2{padding-left:142px;font-weight:700}
.hero-caption .l3{padding-left:200px}
.slider-arrow{top:217px;width:50px;height:50px;border-radius:50%;background:rgba(0,0,0,.45)}
.slider-arrow.prev{left:47px}.slider-arrow.next{left:1101px}
.slider-arrow svg{position:absolute;left:15px;top:13px}
.hero-dots{left:572px;top:440px;display:flex;gap:6px}
.hero-dots span{width:14px;height:14px;border-radius:50%;background:var(--white);border:2px solid #999}
.hero-dots .on{background:#555}

/* welcome */
.welcome{top:633px;height:185px;background:var(--band);text-align:center}
.welcome h1{margin-top:15px;font-size:36px;font-weight:400;color:var(--ink)}
.welcome h1 b{font-weight:600}
.welcome h1 .hl{color:var(--blue-dark)}
.welcome p{margin-top:4px;font-size:22px;color:#333;letter-spacing:.5px}
.btn{display:inline-block;color:var(--white);text-align:center}
.btn-join{margin-top:18px;width:118px;height:45px;line-height:45px;background:var(--blue-deep);font-size:19px;border-radius:2px}

/* services */
.services{top:818px;height:527px;background:var(--panel)}
.divider{top:103px;width:2px;height:400px;background:#ccc}
.service{top:87px;width:330px;text-align:center}
.service-icon{width:140px;height:140px;border-radius:50%;margin:0 auto;background:#4a4a4a;position:relative}
.service-icon.blue{background:var(--blue-deep)}
.service-icon svg{position:absolute;left:35px;top:30px}
.service h3{margin-top:26px;font-size:19px;font-weight:400;line-height:1.3;color:#333}
.service h3 span{display:block;color:var(--blue-deep)}
.service p{margin:18px auto 0;width:300px;font-size:13.5px;line-height:1.35;color:#444}
.btn-more{margin-top:44px;width:88px;height:34px;line-height:34px;font-size:13px;background:var(--button-dark)}
.btn-more.blue{background:var(--blue-deep)}

/* banner */
.invest-banner{top:1345px;height:194px;background:linear-gradient(90deg,#2f4f6e 0%,#3f6c92 50%,#6f8fab 75%,#25476a 100%);overflow:hidden}
.invest-banner h2{left:100px;top:36px;font-size:42px;font-weight:300;color:var(--white);line-height:1.2}
.invest-banner h3{left:96px;top:88px;font-size:32px;font-weight:300;color:var(--white);line-height:1.2}
.invest-banner p{left:98px;top:136px;width:760px;font-size:15px;color:var(--white);white-space:nowrap;line-height:1.3}
.btn-banner{left:897px;width:190px;height:41px;line-height:41px;font-size:18px}
.btn-banner.dark{top:45px;background:var(--button-dark)}
.btn-banner.blue{top:117px;background:var(--blue-deep)}

/* about */
.about{top:1539px;height:470px;background:var(--white)}
.monitor{left:97px;top:66px;width:445px;height:357px}
.monitor-screen{left:0;top:0;width:445px;height:290px;background:#1b1b1b;border-radius:8px;padding:12px}
.monitor-screen div{width:100%;height:100%;background:linear-gradient(100deg,#8a8f96,#d9d4cf 55%,#a7aeb6)}
.monitor-stand{left:190px;top:290px;width:66px;height:50px;background:linear-gradient(#cfcfcf,#9a9a9a)}
.monitor-base{left:150px;top:338px;width:146px;height:12px;border-radius:50%;background:#bcbcbc}
.about-text{left:612px;top:64px;width:495px;font-family:"PT Serif",serif}
.about-text h2{font-size:22px;font-weight:700;color:#222;letter-spacing:.5px}
.about-text .lead{margin-top:14px;font-size:11px;color:#555;text-transform:uppercase;line-height:1.5}
.about-text .body{margin-top:10px;font-size:10.5px;color:#888;line-height:1.55;font-family:"Open Sans",sans-serif}
.about-list{margin-top:36px;list-style:none}
.about-list li{font-size:11px;text-transform:uppercase;color:#444;padding:12px 0 12px 24px;border-bottom:1px solid #e6e6e6;position:relative}
.about-list li::before{content:"";position:absolute;left:4px;top:16px;width:8px;height:8px;border-radius:50%;background:var(--accent)}

/* testimonials */
.testimonials{top:2009px;height:409px;background:linear-gradient(180deg,#2a87a3,#1a6f8c)}
.testimonials h2{width:100%;text-align:center;margin-top:35px;font-size:25px;font-weight:600;color:var(--white);letter-spacing:.5px}
.avatar{left:122px;top:125px;width:180px;height:180px;border-radius:50%;background:linear-gradient(#d8d8d8,#9a9a9a);border:4px solid var(--white)}
.quote{left:396px;top:150px;width:670px;font-size:19px;font-style:italic;color:var(--white);line-height:1.45}
.quote cite{color:var(--accent);font-style:italic}
.qmark{font-family:"PT Serif",serif;font-size:72px;color:var(--white);line-height:1}
.qmark.open{left:338px;top:110px}.qmark.close{left:955px;top:300px}
.t-dots{left:536px;top:362px;display:flex;gap:7px}
.t-dots span{width:15px;height:15px;border-radius:50%;background:var(--white)}
.t-dots .on{background:#9bb}

/* footer */
.site-footer{top:2418px;height:253px;background:var(--charcoal)}
.f-col{top:57px;width:226px}
.f-col h4{height:34px;line-height:34px;background:#6a6a6a;color:var(--white);font-size:14px;font-weight:400;padding-left:16px}
.f-col ul{list-style:none;margin:18px 0 0 22px}
.f-col li{font-size:11.5px;color:#aaa;line-height:1.65}
.f-col li::before{content:"·";margin-right:8px}
.f-contact{text-align:center;font-size:12px;color:#aaa;line-height:1.55;margin-top:10px}
.f-contact .phone{font-size:15px;color:#ccc}
.f-contact u{text-decoration:underline}
.f-social{display:flex;gap:12px;margin:16px 0 0 22px}
.f-social span{width:40px;height:40px;border-radius:50%;background:#888}
.f-social .blue{background:#3b5a9a}
.bottom-bar{left:0;top:2671px;width:1200px;height:41px;background:var(--blue-deep);color:var(--white);font-size:11px;line-height:41px;padding-left:126px}
</style>
</head>
<body>

<header class="site-header">
  <div class="abs brand"><span class="brand-mark"></span><span class="brand-name">TALVIROW</span></div>
  <div class="abs social-top"><span></span><span></span><span></span><span></span><span></span></div>
  <nav class="abs main-nav"><span class="current">Home</span><span>About Us</span><span>Services</span><span>Blog</span><span>Contact Us</span></nav>
</header>

<section class="hero">
  <div class="abs hero-photo" role="img" aria-label="Photograph of business people shaking hands in a bright office meeting"></div>
  <div class="abs hero-caption">
    <div>Advice on how</div><div class="l2">to make</div><div class="l3">wise investments</div>
  </div>
  <div class="abs slider-arrow prev"><svg width="20" height="24" viewBox="0 0 20 24"><path d="M16 2 L4 12 L16 22" fill="none" stroke="#fff" stroke-width="4"/></svg></div>
  <div class="abs slider-arrow next"><svg width="20" height="24" viewBox="0 0 20 24"><path d="M4 2 L16 12 L4 22" fill="none" stroke="#fff" stroke-width="4"/></svg></div>
  <div class="abs hero-dots"><span></span><span class="on"></span><span></span></div>
</section>

<section class="welcome">
  <h1>Welcome to <b>Talvirow</b> <b class="hl">LLC</b> !</h1>
  <p>WE CAN BE YOUR GUIDE TO THE WORLD OF INVESTMENTS</p>
  <span class="btn btn-join">Join Us</span>
</section>

<section class="services">
  <div class="abs divider" style="left:427px"></div>
  <div class="abs divider" style="left:771px"></div>
  <div class="abs service" style="left:90px">
    <div class="service-icon blue"><svg width="70" height="80" viewBox="0 0 70 80"><rect x="8" y="4" width="40" height="66" rx="5" fill="#fff"/><rect x="14" y="11" width="28" height="12" fill="#2f6fb3"/><g fill="#2f6fb3"><rect x="14" y="30" width="7" height="7"/><rect x="25" y="30" width="7" height="7"/><rect x="14" y="42" width="7" height="7"/><rect x="25" y="42" width="7" height="7"/><rect x="14" y="54" width="7" height="7"/></g><circle cx="52" cy="56" r="6" fill="none" stroke="#fff" stroke-width="4"/><circle cx="64" cy="72" r="6" fill="none" stroke="#fff" stroke-width="4"/><path d="M66 50 L48 78" stroke="#fff" stroke-width="4"/></svg></div>
    <h3><span>INDIVIDUAL</span>APPROACH</h3>
    <p>Corrupti quos dolores et quas molestias excepturi sint occaecati cupiditate non provident, similique sunt in culpa qui officia</p>
    <span class="btn btn-more blue">Read More</span>
  </div>
  <div class="abs service" style="left:436px">
    <div class="service-icon"><svg width="70" height="80" viewBox="0 0 70 80"><rect x="6" y="8" width="44" height="58" fill="#fff"/><circle cx="40" cy="44" r="14" fill="#4a4a4a" stroke="#fff" stroke-width="4"/><path d="M50 54 L64 70" stroke="#fff" stroke-width="7"/><g stroke="#4a4a4a" stroke-width="3"><path d="M12 18 H40"/><path d="M12 26 H34"/></g></svg></div>
    <h3><span>BUSINESS</span>ANALYTICS</h3>
    <p>Corrupti quos dolores et quas molestias excepturi sint occaecati cupiditate non provident, similique sunt in culpa qui officia</p>
    <span class="btn btn-more">Read More</span>
  </div>
  <div class="abs service" style="left:780px">
    <div class="service-icon"><svg width="70" height="80" viewBox="0 0 70 80"><circle cx="35" cy="16" r="12" fill="#fff"/><path d="M10 72 V46 Q10 32 26 32 H44 Q60 32 60 46 V72 Z" fill="#fff"/><path d="M30 34 L35 60 L40 34 Z" fill="#4a4a4a"/></svg></div>
    <h3><span>INVESTMENT</span>CONSULTING</h3>
    <p>Corrupti quos dolores et quas molestias excepturi sint occaecati cupiditate non provident, similique sunt in culpa qui officia</p>
    <span class="btn btn-more">Read More</span>
  </div>
</section>

<section class="invest-banner" role="img" aria-label="Glass office tower facade in blue tones">
  <h2 class="abs">We Meet Your</h2>
  <h3 class="abs">Financial Investment Needs</h3>
  <p class="abs">Lorem ipsum dolor sit amet, consectetur adipisicing elit, sed do eiusmod tempor incididunt ut labore</p>
  <span class="abs btn btn-banner dark">Join Us</span>
  <span class="abs btn btn-banner blue">Register Now</span>
</section>

<section class="about">
  <div class="abs monitor">
    <div class="abs monitor-screen"><div role="img" aria-label="Photograph of a smiling businesswoman with colleagues in an office"></div></div>
    <div class="abs monitor-stand"></div>
    <div class="abs monitor-base"></div>
  </div>
  <div class="abs about-text">
    <h2>ABOUT COMPANY</h2>
    <p class="lead">We teach you how to improve your business processes, and make the technology affordable for you.</p>
    <p class="body">Sed ut perspiciatis unde omnis iste natus error sit voluptatem accusantium doloremque laudantium, totam rem aperiam, eaque ipsa quae ab illo inventore veritatis et quasi architecto beatae vitae dicta sunt explicabo. Nemo enim ipsam voluptatem quia voluptas sit aspernatur aut odit aut fugit, sed quia consequuntur magni dolores eos qui ratione voluptatem sequi nesciunt.</p>
    <ul class="about-list">
      <li>Sed ut perspiciatis unde omnis iste</li>
      <li>Accusantium doloremque laudant</li>
      <li>Rotam rem aperiam eaque ipsa uae</li>
      <li>Aillo inventore veritatis et quasi</li>
    </ul>
  </div>
</section>

<section class="testimonials">
  <h2>SATISFIED CUSTOMERS</h2>
  <div class="abs avatar" role="img" aria-label="Portrait photograph of a satisfied customer"></div>
  <span class="abs qmark open">“</span>
  <p class="abs quote">Lorem Ipsum is simply dummy text of the printing and typesetting industry. Lorem Ipsum has been the industry's standard dummy text ever since the 1500s, when an unknown printer took a galley of type and scrambled it to make a type specimen book. It has survived not only five centuries, but also the leap into electronic.... <cite>Mr.DANIEL ROSS</cite></p>
  <span class="abs qmark close">”</span>
  <div class="abs t-dots"><span class="on"></span><span></span><span></span><span></span><span></span><span></span></div>
</section>

<footer class="site-footer">
  <div class="abs f-col" style="left:120px">
    <h4>COMPANY</h4>
    <ul><li>About us</li><li>Career</li><li>Our works / References</li><li>Contact us</li></ul>
  </div>
  <div class="abs f-col" style="left:366px">
    <h4>OUR SERVICES</h4>
    <ul><li>Lorem ipsum</li><li>Dolor sit amet</li><li>Nullam in ultricies</li><li>Vestibulum at sapie</li></ul>
  </div>
  <div class="abs f-col" style="left:608px">
    <h4>CONTACT US</h4>
    <div class="f-contact"><div class="phone">+1-415-555-0142,</div><u>Suite 410, 220 Harbor Lane,</u><br><u>Bay Point District,</u><br><u>San Francisco, CA 94105,</u><br><u>USA.</u></div>
  </div>
  <div class="abs f-col" style="left:852px">
    <h4 style="text-align:center;padding-left:0">Social Connections</h4>
    <div class="f-social"><span class="blue"></span><span></span><span></span></div>
  </div>
</footer>
<div class="abs bottom-bar">Copyright 2014 All Right Reserved</div>

</body>
</html>
```